Retail Jewelry Business Card Design Project

We are in need of a new business card design for a retail jewelry store. This store is in the business of fine jewelry including but not specific to bridal jewelry, diamonds, designer jewelry and watches.

This store has been in business for 20 years but continues to strive for a modern professional appeal. The main colors use for this business are a royal blue, white and silver.

Target Market(s)

Target market is ages 18-50

Industry/Entity Type

Jewelry

Requirements
Must have
• Sales Person Name
Sales Person Email Address

Store Address
Store Phone
Website

Standard business card size. No odd shapes or sizes.
Nice to have
• Overall modern feel for card.

We have thought that a design with a nice feature of the logo on the back of the card would be nice but open to ideas.
Should not have
• No specific images of jewelry should be used.

```html
<!DOCTYPE html>
<html lang="en">
<head>
<meta charset="utf-8">
<title>Marlow Reed Fine Jewelry – Stationery</title>
<link href="https://fonts.googleapis.com/css2?family=Cinzel:wght@400;700&display=swap" rel="stylesheet">
<style>
  :root {
    --backdrop: #f2f2f2;
    --paper: #ffffff;
    --royal: #7370b3;
    --royal-deep: #3b3880;
    --ink: #3a3a3a;
    --silver-dark: #b6b7ba;
    --silver-light: #f4f4f4;
    --edge: #dcdcdc;
  }
  * { margin: 0; padding: 0; box-sizing: border-box; }
  html, body { width: 1200px; height: 900px; overflow: hidden; }
  body { background: var(--backdrop); position: relative; font-family: "Cinzel", serif; }

  .piece { position: absolute; background: var(--paper); overflow: hidden; }
  .piece svg.waves { position: absolute; inset: 0; width: 100%; height: 100%; }

  .card-front { left: 196px; top: 86px; width: 336px; height: 202px; border-left: 1px solid var(--edge); }
  .card-back  { left: 196px; top: 342px; width: 336px; height: 202px; border: 1px solid var(--edge); }
  .letterhead { left: 597px; top: 61px; width: 407px; height: 525px; }
  .envelope   { left: 367px; top: 619px; width: 469px; height: 220px; border: 1px solid var(--edge); }

  .brand { position: absolute; color: var(--royal-deep); font-weight: 700; text-align: center; line-height: 1.05; }
  .brand .brand-name { display: block; }
  .brand .brand-line { display: block; letter-spacing: 0.14em; }
  .card-front .brand { left: 0; right: 0; top: 80px; }
  .card-front .brand-name { font-size: 27px; }
  .card-front .brand-line { font-size: 10px; margin-top: 4px; }
  .letterhead .brand { right: 30px; top: 30px; }
  .letterhead .brand-name { font-size: 18px; }
  .letterhead .brand-line { font-size: 7px; margin-top: 3px; }
  .envelope .brand { right: 22px; top: 170px; }
  .envelope .brand-name { font-size: 16px; }
  .envelope .brand-line { font-size: 6px; margin-top: 2px; }

  .contact { position: absolute; font-size: 10px; line-height: 14px; color: var(--ink); }
  .contact .accent { color: var(--royal); }
  .contact .web { font-size: 9px; }
  .card-back .store { left: 32px; top: 54px; }
  .card-back .person { right: 28px; top: 136px; text-align: right; }
  .card-back .person .name { font-size: 10px; color: var(--royal); }
  .card-back .person .email { font-size: 7px; }
  .letterhead .contact { left: 25px; top: 446px; font-size: 10.5px; }

  .address-line { position: absolute; height: 2px; }
  .address-line.primary { left: 33px; top: 86px; width: 158px; background: var(--royal); }
  .address-line.secondary { left: 33px; top: 105px; width: 228px; background: var(--silver-dark); }
</style>
</head>
<body>

<!-- Business card, front -->
<section class="piece card-front">
  <svg class="waves" viewBox="0 0 336 202" preserveAspectRatio="none" aria-hidden="true">
    <defs>
      <linearGradient id="silver-front" x1="0" x2="1">
        <stop offset="0" stop-color="var(--silver-dark)"/>
        <stop offset="0.45" stop-color="var(--silver-light)"/>
        <stop offset="1" stop-color="var(--silver-dark)"/>
      </linearGradient>
    </defs>
    <path d="M0 0 H336 C250 6 130 52 0 68 Z" fill="var(--royal)"/>
    <path d="M0 38 C110 38 210 14 336 0 C240 10 130 50 0 54 Z" fill="url(#silver-front)"/>
    <path d="M80 202 C170 172 260 158 336 166 V202 Z" fill="var(--royal)"/>
  </svg>
  <div class="brand">
    <span class="brand-name">Marlow Reed</span>
    <span class="brand-line">Fine Jewelry</span>
  </div>
</section>

<!-- Business card, back -->
<section class="piece card-back">
  <svg class="waves" viewBox="0 0 336 202" preserveAspectRatio="none" aria-hidden="true">
    <defs>
      <linearGradient id="silver-back" x1="0" x2="1">
        <stop offset="0" stop-color="var(--silver-dark)"/>
        <stop offset="0.5" stop-color="var(--silver-light)"/>
        <stop offset="1" stop-color="var(--silver-dark)"/>
      </linearGradient>
    </defs>
    <path d="M20 0 H336 V68 C240 66 130 20 20 0 Z" fill="var(--silver-dark)"/>
    <path d="M60 0 H336 V58 C240 56 150 24 60 0 Z" fill="var(--royal)"/>
    <path d="M60 0 H336 V38 C250 38 150 18 60 0 Z" fill="url(#silver-back)"/>
    <path d="M0 164 C90 158 180 176 250 202 H0 Z" fill="url(#silver-back)"/>
  </svg>
  <div class="contact store">
    <div class="accent">Marlow Reed Fine</div>
    <div>2280 Lindell Avenue</div>
    <div class="accent">Harbor Point, FL 32990</div>
    <div class="web">www.marlowreedjewelry.com</div>
  </div>
  <div class="contact person">
    <div class="name">Marlow Reed Whitaker</div>
    <div class="email">marlow@marlowreedjewelry.com</div>
  </div>
</section>

<!-- Letterhead -->
<section class="piece letterhead">
  <svg class="waves" viewBox="0 0 407 525" preserveAspectRatio="none" aria-hidden="true">
    <defs>
      <linearGradient id="silver-letter" x1="0" x2="1">
        <stop offset="0" stop-color="var(--silver-dark)"/>
        <stop offset="0.45" stop-color="var(--silver-light)"/>
        <stop offset="1" stop-color="var(--silver-dark)"/>
      </linearGradient>
    </defs>
    <path d="M0 0 H336 C250 20 150 60 0 62 Z" fill="url(#silver-letter)"/>
    <path d="M0 0 H336 C250 14 150 44 0 44 Z" fill="var(--royal)"/>
    <path d="M190 525 C270 500 340 486 407 486 V525 Z" fill="url(#silver-letter)"/>
    <path d="M200 525 C280 506 350 496 407 498 V525 Z" fill="var(--royal)"/>
  </svg>
  <div class="brand">
    <span class="brand-name">Marlow Reed</span>
    <span class="brand-line">Fine Jewelry</span>
  </div>
  <div class="contact">
    <div>2280 Lindell Avenue</div>
    <div class="accent">Harbor Point, FL 32990</div>
    <div class="web">www.marlowreedjewelry.com</div>
    <div class="accent web">marlow@marlowreedjewelry.com</div>
  </div>
</section>

<!-- Envelope -->
<section class="piece envelope">
  <svg class="waves" viewBox="0 0 469 220" preserveAspectRatio="none" aria-hidden="true">
    <defs>
      <linearGradient id="silver-env" x1="0" x2="1">
        <stop offset="0" stop-color="var(--silver-dark)"/>
        <stop offset="0.5" stop-color="var(--silver-light)"/>
        <stop offset="1" stop-color="var(--silver-dark)"/>
      </linearGradient>
    </defs>
    <path d="M20 0 H469 V72 C330 70 180 26 20 0 Z" fill="var(--silver-dark)"/>
    <path d="M80 0 H469 V60 C330 58 200 26 80 0 Z" fill="var(--royal)"/>
    <path d="M80 0 H469 V40 C340 40 200 20 80 0 Z" fill="url(#silver-env)"/>
    <path d="M0 182 C120 176 240 196 350 220 H0 Z" fill="url(#silver-env)"/>
  </svg>
  <div class="address-line primary"></div>
  <div class="address-line secondary"></div>
  <div class="brand">
    <span class="brand-name">Marlow Reed</span>
    <span class="brand-line">Fine Jewelry</span>
  </div>
</section>

</body>
</html>
```